Summit Builders Web Site / Business Cards

Construction Company that specializes in Water and Fire Damage, Residential ReModels, Landscaping and Building ADU (Accessory Dwelling Unit)

Growing and changing families often need additional space, and a remodeling project can often provide that. Adding a new area, or repurposing an existing one can satisfy this requirement.

Other times, homeowners want to update the look in their kitchen or bathroom with more than just a change of cabinetry or vanity doors and drawers. Whatever your needs are, Summit Builders has skilled workers who are bonded and insured, and ready to make your dreams and visions a reality.

Target Market(s)

Home Owners

Industry/Entity Type

Construction Company

Contact Information for Business Card

Center Logo with our information on the corners

Back side to be Logo Only
Contact Info
CSLB License # 4829516
info@summitbuildersca.example
www.summitbuildersca.example

Coding

Coded - Design and coding required

Number of Pages Required

5+ page

Font styles to use
Serif
Sans Serif

Requirements
Must have
• Using our Logo Colors
Home
About Us
Services
Projects / Portfolio
Contact Us
Nice to have
• Colors matching our Logo
Should not have
• Black because it doesnt match our logo

```html
<!DOCTYPE html>
<html lang="en">
<head>
<meta charset="utf-8">
<title>Summit Builders — Construction &amp; Remodeling</title>
<link href="https://fonts.googleapis.com/css2?family=Oswald:wght@400;500;600;700&family=Poppins:wght@400;500;600&display=swap" rel="stylesheet">
<style>
:root{
  --orange:#fa6a0a;
  --orange-soft:#fde6d6;
  --orange-light:#ffb27a;
  --rust:#7a2c05;
  --rust-deep:#5a2104;
  --ink:#2e2622;
  --text:#5a524e;
  --white:#fff;
}
*{box-sizing:border-box;margin:0;padding:0}
html,body{width:1200px;height:4930px;overflow:hidden}
body{position:relative;background:var(--white);font-family:"Poppins",sans-serif;color:var(--text)}
.abs{position:absolute}
.head{font-family:"Oswald",sans-serif;font-weight:600;color:var(--ink);text-transform:uppercase;line-height:1.05}
.label{font-family:"Oswald",sans-serif;font-weight:500;color:var(--orange);font-size:15px;text-transform:uppercase;border-left:2px solid var(--orange);padding-left:10px;line-height:30px}
.label.on-dark{color:var(--orange-light);border-color:var(--orange-light)}
.btn{background:var(--orange);color:var(--white);font-family:"Poppins",sans-serif;font-weight:600;font-size:13px;text-transform:uppercase;display:flex;align-items:center;justify-content:center}
.photo{position:absolute}
p.body{font-size:15.5px;line-height:24px;color:var(--text)}

/* top bar & header */
.topbar{left:0;top:0;width:1200px;height:44px;background:var(--orange)}
.topbar .info{position:absolute;top:0;height:44px;display:flex;align-items:center;gap:8px;color:var(--white);font-size:12.5px;font-weight:500}
.brand-block{left:0;top:0;width:360px;height:147px;background:var(--white);clip-path:polygon(0 0,100% 0,66% 100%,0 100%)}
.brand{left:14px;top:62px;display:flex;align-items:center;gap:14px}
.brand .mark{width:40px;height:40px;background:var(--orange)}
.brand .name{font-family:"Oswald",sans-serif;font-weight:700;font-size:27px;color:var(--ink);line-height:1}
.nav{left:502px;top:84px;display:flex;gap:40px;font-family:"Oswald",sans-serif;font-weight:500;font-size:15px;color:var(--ink);text-transform:uppercase;white-space:nowrap}

/* hero */
.hero{left:0;top:147px;width:1200px;height:642px;background:linear-gradient(100deg,#4a3a2c 0%,#6b5642 35%,#a9a7a1 60%,#d4cec4 100%)}
.hero-arrow{top:448px;width:42px;height:42px;background:rgba(255,255,255,.15);display:flex;align-items:center;justify-content:center}

/* process */
.step{width:146px;height:126px;border:2px dashed var(--orange);display:flex;align-items:center;justify-content:center}
.step-num{width:40px;height:40px;border-radius:50%;background:var(--orange);color:var(--white);font-weight:600;font-size:17px;display:flex;align-items:center;justify-content:center}
.step-title{font-family:"Oswald",sans-serif;font-weight:600;font-size:20px;color:var(--ink);text-transform:uppercase;width:330px;text-align:center}
.step-text{font-size:14px;line-height:22px;width:330px;text-align:center}

/* services */
.services{left:0;top:2035px;width:1102px;height:625px;background:var(--rust)}
.services-strip{left:1110px;top:2035px;width:90px;height:625px;background:var(--orange)}
.svc-name{font-family:"Oswald",sans-serif;font-weight:600;font-size:27px;color:var(--white);text-transform:uppercase;width:251px;text-align:center}

/* footer */
.signup{left:0;top:4339px;width:1200px;height:184px;background:var(--orange)}
.footer{left:0;top:4523px;width:1200px;height:407px;background:var(--rust-deep)}
.f-head{font-family:"Oswald",sans-serif;font-weight:600;font-size:17px;color:var(--white);text-transform:uppercase}
.f-list{list-style:none;font-size:14px;line-height:27px;color:#f3dccd}
.f-rule{width:1px;height:190px;background:rgba(255,255,255,.2)}
</style>
</head>
<body>

<!-- top bar -->
<div class="abs topbar">
  <div class="info" style="left:404px">
    <svg width="14" height="14" viewBox="0 0 14 14"><circle cx="7" cy="7" r="6" fill="none" stroke="#fff" stroke-width="1.6"/><path d="M7 3.5V7l2.4 1.6" stroke="#fff" stroke-width="1.6" fill="none"/></svg>
    Opening Times: 8:00 Am-12:00 Pm
  </div>
  <div class="info" style="left:700px">
    <svg width="13" height="13" viewBox="0 0 24 24"><path d="M6.6 10.8a15 15 0 006.6 6.6l2.2-2.2c.3-.3.7-.4 1-.2 1.1.4 2.3.6 3.6.6.6 0 1 .4 1 1V20c0 .6-.4 1-1 1A17 17 0 013 4c0-.6.4-1 1-1h3.5c.6 0 1 .4 1 1 0 1.3.2 2.5.6 3.6.1.3 0 .7-.2 1z" fill="#fff"/></svg>
    Call Us: 555 014 2290
  </div>
  <div class="info" style="left:962px">
    <svg width="12" height="13" viewBox="0 0 12 13"><circle cx="6" cy="3.5" r="3" fill="#fff"/><path d="M0 13c0-3.5 2.7-5.5 6-5.5s6 2 6 5.5z" fill="#fff"/></svg>
    LOGIN FOR MEMBERS
  </div>
</div>
<div class="abs brand-block"></div>
<div class="abs brand"><div class="mark"></div><div class="name">SUMMIT BUILDERS</div></div>
<nav class="abs nav"><span>Home</span><span>About Us</span><span>Our Services</span><span>Projects / Portfolio</span><span>Contact Us</span></nav>
<svg class="abs" style="left:1094px;top:86px" width="18" height="18" viewBox="0 0 18 18"><circle cx="7.5" cy="7.5" r="5.5" fill="none" stroke="#2e2622" stroke-width="2"/><path d="M12 12l4.5 4.5" stroke="#2e2622" stroke-width="2"/></svg>

<!-- hero -->
<div class="abs hero" role="img" aria-label="Photo of a construction engineer in a hard hat on the phone in front of a residential building, excavator at left"></div>
<div class="abs hero-arrow" style="left:8px"><svg width="10" height="14" viewBox="0 0 10 14"><path d="M8 1L2 7l6 6" stroke="#fff" stroke-width="2" fill="none"/></svg></div>
<div class="abs hero-arrow" style="left:1150px"><svg width="10" height="14" viewBox="0 0 10 14"><path d="M2 1l6 6-6 6" stroke="#fff" stroke-width="2" fill="none"/></svg></div>
<div class="abs label" style="left:86px;top:303px;font-size:17px">Great Experience in Building.</div>
<div class="abs head" style="left:84px;top:350px;font-size:84px;color:#fff;line-height:.93;font-weight:700">Build a<br>Better World</div>
<p class="abs" style="left:86px;top:520px;width:470px;color:#fff;font-size:15.5px;line-height:20px">Sed do eiusmod tempor incididunt ut labore et dolore magna aliqua ut enim</p>
<div class="abs btn" style="left:86px;top:589px;width:161px;height:46px">Start Free Trial</div>

<!-- about -->
<div class="abs head" style="left:163px;top:840px;font-size:98px;color:#f2f2f2;font-weight:700">About Us</div>
<div class="photo" style="left:90px;top:903px;width:250px;height:575px;background:linear-gradient(160deg,#c9702b,#e8853a 45%,#6fa7d3);clip-path:polygon(100% 0,100% 100%,0 100%,0 17%)" role="img" aria-label="Photo of orange steel crane structure against blue sky"></div>
<div class="photo" style="left:359px;top:903px;width:250px;height:575px;background:linear-gradient(180deg,#4b86c5,#e5b400 35%,#5b4c3a 75%,#6e5f52);clip-path:polygon(0 0,100% 17%,100% 100%,0 100%)" role="img" aria-label="Photo of a welder in a yellow helmet working on rebar"></div>
<div class="abs label" style="left:683px;top:978px">Where Can We Help You</div>
<div class="abs head" style="left:683px;top:1022px;font-size:38px;font-weight:700">Welcome to Construction<br>Real Solutions.</div>
<p class="abs body" style="left:683px;top:1114px;width:440px">Sed do eiusmod tempor incididunt ut labore et dolore magna aliqua. Ut enim ad minim veniam, quis derit in voluptate velit esse cillum dolore eu fugiat nullaatur. Excepteur sint occaecat &nbsp;non proident, sunt in culpa qui officia deserunt</p>
<p class="abs body" style="left:683px;top:1258px;width:440px">mollit anim id est laborum. Sed ut perspiciatis unde omnis iste natus error sit voluptatem<br>dolor emque laudantium...</p>
<div class="abs btn" style="left:683px;top:1349px;width:161px;height:48px">Read More</div>

<!-- process -->
<div class="abs label" style="left:529px;top:1584px">Our Work Process</div>
<div class="abs head" style="left:0;width:1200px;text-align:center;top:1622px;font-size:38px">How Does Summit Builders Works</div>

<div class="abs step" style="left:161px;top:1717px">
  <svg width="46" height="46" viewBox="0 0 46 46" fill="none" stroke="#fa6a0a" stroke-width="2"><rect x="6" y="4" width="26" height="36"/><path d="M11 12h16M11 18h16M11 24h10M11 30h8"/><path d="M37 8v30l3 4 3-4V8z"/></svg>
</div>
<div class="abs step-num" style="left:285px;top:1697px">1</div>
<div class="abs step" style="left:528px;top:1717px">
  <svg width="46" height="46" viewBox="0 0 46 46" fill="none" stroke="#fa6a0a" stroke-width="2"><rect x="4" y="6" width="38" height="26"/><path d="M23 32v8M15 40h16"/><circle cx="23" cy="19" r="6"/><path d="M23 11v2M23 25v2M15 19h2M29 19h2"/></svg>
</div>
<div class="abs step-num" style="left:652px;top:1697px">2</div>
<div class="abs step" style="left:892px;top:1717px">
  <svg width="46" height="46" viewBox="0 0 46 46" fill="none" stroke="#fa6a0a" stroke-width="2"><rect x="6" y="22" width="34" height="8"/><rect x="10" y="30" width="26" height="8"/><path d="M12 22l3-6h16l3 6"/><circle cx="23" cy="10" r="4"/></svg>
</div>
<div class="abs step-num" style="left:1016px;top:1697px">3</div>
<svg class="abs" style="left:340px;top:1750px" width="150" height="40" viewBox="0 0 150 40" fill="none" stroke="#c9c9c9" stroke-width="1.5" stroke-dasharray="4 4"><path d="M2 34Q70 -6 140 14"/><path d="M134 8l7 6-8 4" stroke-dasharray="0"/></svg>
<svg class="abs" style="left:712px;top:1750px" width="150" height="40" viewBox="0 0 150 40" fill="none" stroke="#c9c9c9" stroke-width="1.5" stroke-dasharray="4 4"><path d="M2 8Q70 50 140 26"/><path d="M132 20l8 6-7 6" stroke-dasharray="0"/></svg>

<div class="abs step-title" style="left:68px;top:1865px">General Contract</div>
<p class="abs step-text" style="left:68px;top:1908px">Lorem Ipsum is simply dummy text of the and typesetting industry.</p>
<div class="abs step-title" style="left:435px;top:1865px">Project Planing</div>
<p class="abs step-text" style="left:435px;top:1908px">Lorem Ipsum is simply dummy text of the and typesetting industry.</p>
<div class="abs step-title" style="left:799px;top:1865px">Interior Design</div>
<p class="abs step-text" style="left:799px;top:1908px">Lorem Ipsum is simply dummy text of the and typesetting industry.</p>

<!-- services -->
<div class="abs services"></div>
<div class="abs services-strip"></div>
<div class="abs label on-dark" style="left:88px;top:2144px">What We Offer</div>
<div class="abs head" style="left:88px;top:2186px;font-size:38px;color:#fff;font-weight:700">Summit Builders<br>Best Services</div>
<div class="photo" style="left:88px;top:2283px;width:251px;height:228px;background:linear-gradient(180deg,#7ea8cf,#d9dde0 50%,#5f8a4d)" role="img" aria-label="Photo of a modern two-storey home with lawn"></div>
<div class="photo" style="left:358px;top:2283px;width:251px;height:228px;background:linear-gradient(180deg,#b6cde3,#c98d55 45%,#8a5a33)" role="img" aria-label="Photo of a timber house frame under construction"></div>
<div class="photo" style="left:626px;top:2283px;width:251px;height:228px;background:linear-gradient(180deg,#4d7a36,#7fa45a 50%,#556e3d)" role="img" aria-label="Photo of a landscaped garden with stone path and pond"></div>
<div class="photo" style="left:894px;top:2283px;width:251px;height:228px;background:linear-gradient(180deg,#2fb7d4,#6fd5e6 60%,#b89b7a)" role="img" aria-label="Photo of a swimming pool ladder"></div>
<div class="abs svc-name" style="left:88px;top:2522px">Building ADU</div>
<div class="abs svc-name" style="left:358px;top:2522px">Residential</div>
<div class="abs svc-name" style="left:626px;top:2522px">Landscaping</div>
<div class="abs svc-name" style="left:894px;top:2522px">Water</div>

<!-- commitment -->
<div class="abs label" style="left:88px;top:2838px">Explore the Features</div>
<div class="abs head" style="left:88px;top:2880px;font-size:38px">Project Commitment</div>
<p class="abs body" style="left:88px;top:2936px;width:440px">Sed do eiusmod tempor incididunt ut labore et dolore magna aliqua. Ut enim ad minim veniam, quis derit in voluptate velit esse cillum dolore eu fugiat nullaatur. Excepteur sint occaecat &nbsp;non proident, sunt in culpa qui officia deserunt...</p>
<div class="abs btn" style="left:88px;top:3083px;width:161px;height:46px">Read More</div>
<div class="abs" style="left:586px;top:2804px;width:524px;height:354px;background:#fff;border:1px solid #eee;border-radius:22px;box-shadow:0 8px 30px rgba(0,0,0,.12)"></div>
<div class="photo" style="left:637px;top:2827px;width:416px;height:310px;background:linear-gradient(160deg,#d9a441,#f08a2c 45%,#6a5a4c 75%,#d7d2c8)" role="img" aria-label="Photo of three engineers in hard hats reviewing plans"></div>

<!-- recent projects -->
<div class="abs label" style="left:153px;top:3315px">Our Work</div>
<div class="abs head" style="left:153px;top:3356px;font-size:38px">Explore Recent Projects</div>
<div class="photo" style="left:593px;top:3271px;width:220px;height:209px;background:linear-gradient(160deg,#c8b9a0,#8c7a5f 55%,#e3b21f)" role="img" aria-label="Photo of a worker holding a hard hat near an excavator"></div>
<div class="photo" style="left:833px;top:3271px;width:220px;height:209px;background:linear-gradient(180deg,#7fa05b,#8f5e3d 45%,#4f8b35)" role="img" aria-label="Photo of a backyard pergola with lawn"></div>
<div class="photo" style="left:153px;top:3499px;width:220px;height:205px;background:#6b4a33" role="img" aria-label="Photo of construction tools"></div>
<div class="abs" style="left:162px;top:3508px;width:202px;height:187px;border:2px solid #fff"></div>
<div class="abs" style="left:221px;top:3582px;width:36px;height:36px;border-radius:50%;background:#fff;display:flex;align-items:center;justify-content:center"><svg width="14" height="14" viewBox="0 0 14 14"><circle cx="6" cy="6" r="4" fill="none" stroke="#2e2622" stroke-width="1.8"/><path d="M9 9l4 4" stroke="#2e2622" stroke-width="1.8"/></svg></div>
<div class="abs" style="left:263px;top:3582px;width:36px;height:36px;border-radius:50%;background:#fff;display:flex;align-items:center;justify-content:center"><svg width="14" height="14" viewBox="0 0 14 14" fill="none" stroke="#2e2622" stroke-width="1.8"><path d="M6 8l2-2"/><path d="M5 6L3 8a2 2 0 003 3l2-2"/><path d="M9 8l2-2a2 2 0 00-3-3L6 5"/></svg></div>
<div class="photo" style="left:392px;top:3499px;width:421px;height:329px;background:linear-gradient(180deg,#7c9c68,#eaeaea 45%,#6a4b34 80%,#5b7240)" role="img" aria-label="Photo of a small modern backyard cottage"></div>
<div class="photo" style="left:833px;top:3499px;width:220px;height:205px;background:linear-gradient(160deg,#d8a877,#a8703f 60%,#6c4a2e)" role="img" aria-label="Photo of interior timber framing"></div>
<div class="photo" style="left:833px;top:3723px;width:220px;height:206px;background:linear-gradient(160deg,#e6e6e6,#e55b1a 50%,#6a5a4c)" role="img" aria-label="Photo of a worker holding an orange hard hat"></div>

<!-- testimonial -->
<div class="abs head" style="left:163px;top:3880px;font-size:420px;color:var(--orange-soft);font-family:Georgia,serif;font-weight:700;line-height:1">&ldquo;</div>
<div class="photo" style="left:546px;top:3939px;width:108px;height:108px;border-radius:50%;background:linear-gradient(180deg,#8a7a6c,#5a4a3e)" role="img" aria-label="Portrait photo of Dan Morrow"></div>
<div class="abs head" style="left:0;width:1200px;text-align:center;top:4060px;font-size:27px">Dan Morrow</div>
<div class="abs" style="left:0;width:1200px;text-align:center;top:4098px;font-size:12px;font-weight:600;color:var(--orange)">MANAGER</div>
<p class="abs body" style="left:270px;width:660px;text-align:center;top:4140px;font-size:15.5px;line-height:22px">Sed do eiusmod tempor incididunt ut labore et dolore magna aliqua.<br>Ut enim ad minim veniam, quis derit in voluptate velit esse cillum dolore eu fugiat nullaatur. Excepteur sint occaecat cupidatat</p>
<div class="abs" style="left:506px;top:4248px;width:58px;height:2px;background:#d0d0d0"></div>
<div class="abs" style="left:572px;top:4247px;width:58px;height:4px;background:var(--orange)"></div>
<div class="abs" style="left:637px;top:4248px;width:58px;height:2px;background:#d0d0d0"></div>

<!-- signup -->
<div class="abs signup"></div>
<div class="abs head" style="left:88px;top:4380px;font-size:38px;color:#fff;font-weight:700;line-height:.95">Sign Up To<br>Get Latest Updates</div>
<p class="abs" style="left:88px;top:4462px;color:#fff;font-size:13px">It is a long established fact that a reader will be distracted by the</p>
<div class="abs" style="left:610px;top:4406px;width:500px;height:56px;background:#fff;display:flex;align-items:center;padding-left:20px;gap:10px;color:#777;font-size:15.5px">
  <svg width="16" height="12" viewBox="0 0 16 12"><rect x="1" y="1" width="14" height="10" fill="none" stroke="#aaa" stroke-width="1.4"/><path d="M1 1l7 6 7-6" fill="none" stroke="#aaa" stroke-width="1.4"/></svg>
  Enter your email address
</div>
<div class="abs btn" style="left:962px;top:4411px;width:144px;height:46px;background:var(--rust);font-size:14px">Subscribe</div>

<!-- footer -->
<div class="abs footer"></div>
<div class="abs" style="left:90px;top:4640px;display:flex;align-items:center;gap:12px">
  <div style="width:28px;height:28px;background:var(--orange)"></div>
  <div style="font-family:Oswald,sans-serif;font-weight:700;font-size:26px;color:#fff;line-height:1.05">SUMMIT<br>BUILDERS</div>
</div>
<div class="abs" style="left:107px;top:4757px;display:flex;gap:10px">
  <span style="width:36px;height:36px;border-radius:50%;background:var(--orange)"></span>
  <span style="width:36px;height:36px;border-radius:50%;background:var(--orange)"></span>
  <span style="width:36px;height:36px;border-radius:50%;background:var(--orange)"></span>
</div>
<div class="abs f-head" style="left:387px;top:4610px">Quick Links</div>
<ul class="abs f-list" style="left:387px;top:4648px"><li>Home</li><li>About Us</li><li>Services</li><li>Projects / Portfolio</li><li>Contact Us</li></ul>
<div class="abs f-rule" style="left:566px;top:4635px"></div>
<div class="abs f-head" style="left:622px;top:4610px">Our Services</div>
<ul class="abs f-list" style="left:622px;top:4648px"><li>Water</li><li>Fire Damage</li><li>Residential ReModels</li><li>Landscaping</li><li>Building ADU</li><li>(Accessory Dwelling Unit)</li></ul>
<div class="abs f-rule" style="left:842px;top:4635px"></div>
<div class="abs f-head" style="left:882px;top:4600px">Contact Us</div>
<div class="abs" style="left:882px;top:4648px;font-size:13px;color:#f3dccd;line-height:19px">
  <div style="display:flex;gap:12px"><svg width="12" height="12" viewBox="0 0 24 24" style="margin-top:3px"><path d="M6.6 10.8a15 15 0 006.6 6.6l2.2-2.2c.3-.3.7-.4 1-.2 1.1.4 2.3.6 3.6.6.6 0 1 .4 1 1V20c0 .6-.4 1-1 1A17 17 0 013 4c0-.6.4-1 1-1h3.5c.6 0 1 .4 1 1 0 1.3.2 2.5.6 3.6.1.3 0 .7-.2 1z" fill="#fa6a0a"/></svg><div><b style="color:#fff">Phone</b><br>+08 555 014 2290</div></div>
  <div style="display:flex;gap:12px;margin-top:12px"><svg width="12" height="10" viewBox="0 0 12 10" style="margin-top:4px"><rect width="12" height="10" fill="#fa6a0a"/><path d="M0 0l6 5 6-5" fill="none" stroke="#5a2104" stroke-width="1.2"/></svg><div><b style="color:#fff">Email</b><br>info@summitbuildersca.example</div></div>
  <div style="display:flex;gap:12px;margin-top:12px"><svg width="12" height="14" viewBox="0 0 12 14" style="margin-top:3px"><path d="M6 0a5 5 0 015 5c0 4-5 9-5 9S1 9 1 5a5 5 0 015-5z" fill="#fa6a0a"/><circle cx="6" cy="5" r="1.8" fill="#5a2104"/></svg><div><b style="color:#fff">Location</b><br>Some address line goes here<br>city name country</div></div>
</div>
<div class="abs" style="left:1130px;top:4799px;width:46px;height:46px;border-radius:50%;background:var(--orange);display:flex;align-items:center;justify-content:center"><svg width="12" height="8" viewBox="0 0 12 8"><path d="M1 7l5-5 5 5" fill="none" stroke="#fff" stroke-width="2"/></svg></div>
<div class="abs" style="left:0;width:1200px;top:4893px;text-align:center;font-size:13px;color:#f3dccd">© 2020 Copyright - Summit Builders All Rights Reserved</div>

</body>
</html>
```